The Builders Group for Structures and Shelter Systems

The Brochure need to have all the company information and our three products with features and specifications.

1- Sandline Cube
2- Sandline Ridge
3- Sandline Vault

We build movable fast build up houses, we are creative and innovative in making designs. we are ECO friendly to the environment. we have an experienced team. We work in Saudi Arabia. we build large number of luxurious houses for hotels and resorts.

Target Market(s)

Hospitality, Tourism, Real State, Saudi Arabia, Mega projects,

Industry/Entity Type

Residential Construction

Font styles to use
Serif

Colors

Designer to choose colors to be used in the design.

Requirements
Must have
• who we are, what we do vision mission values, Products part. Features part, pictures ,our clients our team contact us. Slogan
Nice to have
• it will be decided later
Should not have
• It will be deiced later

```html
<!DOCTYPE html>
<html lang="en">
<head>
<meta charset="utf-8">
<title>The Builders Group — Brochure Spread</title>
<link rel="stylesheet" href="https://fonts.googleapis.com/css2?family=Montserrat:wght@400;600;700&family=Crimson+Text:wght@400;600&display=swap">
<style>
  :root {
    --backdrop: #ececea;
    --paper: #ffffff;
    --brand-blue: #1f9ad8;
    --brand-blue-soft: rgba(40, 140, 215, 0.78);
    --brand-green: #5cb547;
    --ink: #2b2b2b;
    --white: #ffffff;
  }
  * { box-sizing: border-box; margin: 0; padding: 0; }
  html, body {
    width: 1200px; height: 880px; overflow: hidden;
    background: var(--backdrop);
  }
  .spread {
    position: absolute; left: 40px; top: 220px;
    width: 1120px; height: 440px;
    display: flex;
    box-shadow: 0 10px 30px rgba(0,0,0,0.18);
  }
  .page { position: relative; width: 560px; height: 440px; overflow: hidden; background: var(--paper); }

  /* Left page */
  .about-photo {
    position: absolute; left: 0; top: 0; width: 255px; height: 100%;
    background: linear-gradient(180deg, #2f6fb3 0%, #8fb7d9 22%, #b98f6a 38%, #e9e6e1 55%, #d8b9a0 78%, #c9a58a 100%);
  }
  .about-text { position: absolute; left: 290px; top: 26px; width: 245px; }
  .section-title {
    font-family: "Montserrat", sans-serif; font-weight: 700;
    color: var(--brand-blue); font-size: 20px; letter-spacing: 0.5px;
    margin-left: 12px; margin-bottom: 10px;
  }
  .about-body {
    font-family: "Crimson Text", serif; font-size: 11.5px; line-height: 1.32;
    color: var(--ink);
  }
  .product-photo {
    position: absolute; left: 315px; top: 215px; width: 215px; height: 130px;
    background: linear-gradient(180deg, #f2f2f2 0%, #dedede 60%, #c4c4c4 100%);
  }
  .vision-label {
    position: absolute; left: 0; top: 338px; width: 255px; height: 30px;
    background: var(--brand-blue-soft);
    font-family: "Montserrat", sans-serif; color: var(--white);
    font-size: 14px; letter-spacing: 1px; padding: 6px 0 0 32px;
  }
  .vision-statement {
    position: absolute; left: 0; top: 368px; width: 505px; height: 36px;
    background: var(--brand-green);
    font-family: "Montserrat", sans-serif; font-weight: 700; color: var(--white);
    font-size: 13px; padding: 9px 0 0 34px; white-space: nowrap;
  }

  /* Right page */
  .mission-photo {
    position: absolute; inset: 0;
    background: linear-gradient(180deg, #8fb1d3 0%, #c7d6e3 35%, #d9dde0 48%, #a9a49a 62%, #8b8375 75%, #7a6a55 88%, #6c5c48 100%);
  }
  .mission-box {
    position: absolute; left: 40px; top: 30px; width: 470px; height: 66px;
    background: var(--brand-green); color: var(--white); text-align: center;
    font-family: "Montserrat", sans-serif;
  }
  .mission-box h2 { font-size: 16px; font-weight: 700; letter-spacing: 1px; padding-top: 6px; }
  .mission-rule { width: 150px; height: 1px; background: rgba(255,255,255,0.8); margin: 4px auto 5px; }
  .mission-box p { font-size: 11px; line-height: 1.3; white-space: nowrap; }
  .beliefs {
    position: absolute; left: 6px; top: 120px; width: 548px; text-align: center;
    font-family: "Montserrat", sans-serif; font-size: 10.3px; line-height: 1.5;
    color: var(--brand-blue); white-space: nowrap;
  }
  .beliefs strong { font-weight: 700; }
  .themes { position: absolute; left: 30px; top: 300px; width: 520px; }
  .themes-title {
    height: 22px; background: var(--brand-green); color: var(--white); text-align: center;
    font-family: "Montserrat", sans-serif; font-weight: 700; font-size: 11px; padding-top: 4px;
  }
  .themes-list { display: flex; gap: 4px; margin-top: 3px; }
  .theme {
    flex: 1; height: 42px; background: var(--brand-blue-soft); color: var(--white);
    font-family: "Montserrat", sans-serif; font-size: 9.5px; line-height: 1.2;
    display: flex; align-items: center; justify-content: center; text-align: center;
  }
</style>
</head>
<body>
  <main class="spread">
    <section class="page page-left">
      <div class="about-photo" role="img" aria-label="Photo of a white star-shaped container house in a rocky desert under a blue sky"></div>
      <div class="about-text">
        <h2 class="section-title">WHO WE ARE?</h2>
        <p class="about-body">The Builders Group is managed by a professional expert Saudi engineers that focuses on bringing an innovation, affordable, environmental housing to the country. The Builders Group aims to provide a solution for housing complexity in the country whether it's for construction companies, hospitality and residency. Owning a living space is not a life dream anymore. We simplified complexity of housing to assure that innovation exists to Impact your way of living.</p>
      </div>
      <div class="product-photo" role="img" aria-label="Photo of a white dome house with glass panels and two visitors beside it"></div>
      <div class="vision-label">VISION</div>
      <div class="vision-statement">To inspire and develop the concept of fast Saudi housing solutions</div>
    </section>

    <section class="page page-right">
      <div class="mission-photo" role="img" aria-label="Photo of a row of dome tents on dry desert ground under a pale sky"></div>
      <div class="mission-box">
        <h2>MISSION</h2>
        <div class="mission-rule"></div>
        <p>To provide a portable housing solutions through an innovative modern design<br>with an expert build up engineers.</p>
      </div>
      <p class="beliefs">We believe in <strong>boundless potential</strong> of Saudi economy. We share the <strong>passion</strong> for <strong>better future</strong>,<br>respect the saudi <strong>environment</strong> and <strong>eco</strong>, celebrate, harness the desire for <strong>partnership</strong><br>and <strong>citizenship</strong> and create robust opportunities for <strong>housing</strong> designs.</p>
      <div class="themes">
        <div class="themes-title">STRATEGIC THEMES</div>
        <div class="themes-list">
          <div class="theme">Promote<br>tourism</div>
          <div class="theme">Promote<br>a new experience<br>of camping</div>
          <div class="theme">Support<br>hospitality</div>
          <div class="theme">Promote<br>construction site<br>communities</div>
          <div class="theme">Promote Business<br>Partnering</div>
        </div>
      </div>
    </section>
  </main>
</body>
</html>
```